Quotation and Scripture Design

We are a marketing firm looking for a graphic designer who is gifted in the merging of typestyles, colors, and composition into images suitable for framing in the home or office. The design criteria is quite simple, (1) keep it fresh without looking dated or religious, and (2) push the envelope a little with good, solid graphic design. Phase one will involve building our inventory of original artwork to fifty or more pieces to be marketed online. For phase two in addition to a line of greeting cards, we will also offer art pieces reproduced by laser engravers, CNC routers, chemical etching, and digital printers. For this reason it is necessary that all art files be submitted in a vector format.

Target Market(s)

Professional women and men who appreciate and purchase gallery quality artwork.

Industry/Entity Type

Graphic Designer

Requirements
Must have
• Selection of the designer will be based on their graphic interruption of the following two quotations.
Quotation No. 1 - Romans 8:28
And we know that all things work together for good to those who love God, to those who are called according to His purpose.
Quotation No. 2 -Jeremiah 29:11
For I know the plans I have for you, declares the Lord. Plans to prosper you and not to harm you. Plans to give you hope and a future.
Design one of these two formats to fit a 8" x10" frame, and the other to fit a 12" x 12" frame.
Nice to have
• Rich colors, fresh typestyles . . . please no Times Roman. Bold, creative composition is what we are looking for.
Should not have
• Dated, religious artwork found in the local bible bookstore is a very good example of what we DO NOT want. If it is not something you would purchase for yourself or a friend, more than likely it won't meet our criteria.

```html
<!DOCTYPE html>
<html lang="en">
<head>
<meta charset="utf-8">
<title>Romans 8:28 Scripture Print</title>
<link rel="stylesheet" href="https://fonts.googleapis.com/css2?family=Jost:ital,wght@0,500;1,700&display=swap">
<style>
  :root {
    --ink-blue: #4a86c6;
    --paper-cream: #ece6d4;
    --paper-blue: #bcd3da;
    --paper-mist: #d6e1dc;
  }
  html, body {
    margin: 0;
    padding: 0;
    width: 927px;
    height: 1200px;
    overflow: hidden;
  }
  .print {
    position: relative;
    width: 927px;
    height: 1200px;
    overflow: hidden;
  }
  .print__backdrop {
    position: absolute;
    inset: 0;
    width: 100%;
    height: 100%;
  }
  .print__reference {
    position: absolute;
    left: 44px;
    top: 64px;
    margin: 0;
    font-family: "Jost", "Futura", sans-serif;
    font-style: italic;
    font-weight: 700;
    font-size: 120px;
    line-height: 1;
    letter-spacing: 1px;
    color: var(--ink-blue);
    white-space: nowrap;
  }
  .print__verse {
    position: absolute;
    right: 62px;
    top: 410px;
    width: 860px;
    margin: 0;
    font-family: "Jost", "Futura", sans-serif;
    font-weight: 500;
    font-size: 58px;
    line-height: 73px;
    letter-spacing: 0.5px;
    text-align: right;
    color: var(--ink-blue);
    transform: rotate(-6deg);
    transform-origin: right top;
  }
  .print__verse span {
    display: block;
    white-space: nowrap;
  }
</style>
</head>
<body>
  <main class="print">
    <svg class="print__backdrop" viewBox="0 0 927 1200" preserveAspectRatio="none"
         role="img" aria-label="Weathered paper texture with a faded pale blue and cream harlequin diamond pattern">
      <defs>
        <linearGradient id="paperWash" x1="0" y1="0" x2="1" y2="1">
          <stop offset="0" stop-color="var(--paper-cream)"/>
          <stop offset="0.45" stop-color="var(--paper-mist)"/>
          <stop offset="1" stop-color="var(--paper-blue)"/>
        </linearGradient>
      </defs>
      <rect width="927" height="1200" fill="url(#paperWash)"/>
    </svg>

    <h1 class="print__reference">Romans 8:28</h1>

    <p class="print__verse">
      <span>And we know</span>
      <span>that all things work</span>
      <span>together for good</span>
      <span>to those who love God,</span>
      <span>to those who are called</span>
      <span>according to His purpose</span>
    </p>
  </main>
</body>
</html>
```